Design Emoji directory website with a modern look

Please design the Emoji directory website to display a nice search box as well as design a nice search suggestion dropdown page. Example when you type keyword in Quorvex.
You can use Emojis in SVG file https://www.filebarrow.com/s/7kq2m9x4pLwz8tr/svg.rar?dl=0 to create designs.
The following are 7 example pages but please make sure the design is UNIQUE.
Main page example
https://glyphpond.info/
Content page example
https://glyphpond.info/smiling-face-with-smiling-eyes/
Category page example
https://glyphpond.info/smileys-and-emotion-category/
Holiday page example
https://glyphpond.info/holidays/
Static pages example
https://glyphpond.info/privacy-policy/
404 page not found example
https://glyphpond.info/category/
Search page example
https://glyphpond.info/?s=exchange+rate
Target Market(s)
web design
Industry/Entity Type
Website
Number of Pages Required
5+ page
Font styles to use
Other font styles liked:
- COMIC NEUE
Colors
Designer to choose colors to be used in the design.
Requirements
Must have
- Please make sure its unique, modern look, clean.
Should not have
- Do not use heavy graphics, we only use CSS style rules and SVG's emojis to make sure the site loads fast.

```html
<!DOCTYPE html>
<html lang="en">
<head>
<meta charset="utf-8">
<title>Glyphora – Emoji Encyclopedia</title>
<link href="https://fonts.googleapis.com/css2?family=Comic+Neue:wght@400;700&family=Roboto:wght@400;500&family=Open+Sans:wght@400&display=swap" rel="stylesheet">
<style>
:root{
  --blue-deep:#1283f5;
  --blue-light:#2ab0fb;
  --page:#f8f8f8;
  --card:#ffffff;
  --card-foot:#f3f3f3;
  --line:#e4e4e4;
  --ink:#3d3d3d;
  --muted:#666;
  --accent:#f2415a;
  --white:#fff;
  --tone-red:#e3475b;
  --tone-blue:#4a90d0;
  --tone-dark:#454b52;
  --tone-grey:#b9c3cb;
  --tone-green:#6aa84f;
  --tone-purple:#8e6bd0;
  --tone-amber:#f0a83a;
  --tone-sky:#9fd0f2;
}
*{margin:0;padding:0;box-sizing:border-box}
html,body{width:723px;height:1200px;overflow:hidden}
body{position:relative;background:var(--page);font-family:"Roboto",sans-serif;color:var(--ink)}
.backdrop{position:absolute;left:0;top:0;width:723px;height:1200px}
.brand{position:absolute;left:48px;top:10px;font-family:"Comic Neue",sans-serif;font-weight:700;font-size:30px;color:var(--white)}
.nav{position:absolute;top:20px;left:295px;display:flex;gap:34px;font-size:11.5px;color:var(--white)}
.nav a{color:inherit;text-decoration:none;position:relative}
.nav a.current::after{content:"";position:absolute;left:11px;right:11px;bottom:-7px;height:1.5px;background:var(--white)}
.hero-title{position:absolute;top:100px;width:723px;text-align:center;font-family:"Comic Neue",sans-serif;font-weight:700;font-size:40px;color:var(--white)}
.hero-sub{position:absolute;top:148px;width:723px;text-align:center;font-family:"Comic Neue",sans-serif;font-weight:700;font-size:25px;color:var(--white)}
.hero-lede{position:absolute;top:185px;width:723px;text-align:center;font-size:12.5px;color:var(--white)}
.search{position:absolute;left:164px;top:221px;width:402px;height:34px;border-radius:17px;background:var(--white);display:flex;align-items:center;padding-left:13px;gap:8px;font-size:11.5px;color:#555}
.hero-art{position:absolute;border-radius:40%}
.hero-art.rider{left:88px;top:282px;width:84px;height:84px;background:linear-gradient(150deg,#7cbf5e,#b8714f)}
.hero-art.surfer{left:550px;top:282px;width:88px;height:80px;background:linear-gradient(160deg,#f2b840,#94cf80)}
.card{position:absolute;width:190px;height:190px;background:var(--card);border:1px solid var(--line);box-shadow:0 1px 2px rgba(0,0,0,.12);display:flex;flex-direction:column}
.card-head{height:37px;border-bottom:1px solid var(--line);padding:10px 0 0 17px;font-family:"Comic Neue",sans-serif;font-weight:700;font-size:14px;color:#444}
.card-grid{flex:1;display:grid;grid-template-columns:repeat(3,1fr);padding:9px 10px 0;row-gap:4px}
.item{display:flex;flex-direction:column;align-items:center;gap:3px}
.glyph{width:32px;height:32px;border-radius:8px}
.glyph.round{border-radius:50%}
.glyph.flag{width:44px;height:31px;border-radius:4px}
.label{font-family:"Open Sans",sans-serif;font-size:7.2px;color:var(--muted)}
.card-foot{height:28px;background:var(--card-foot);text-align:center;line-height:28px;font-family:"Comic Neue",sans-serif;font-weight:700;font-size:11px;color:var(--accent);letter-spacing:.4px}
.red{background:var(--tone-red)}.blue{background:var(--tone-blue)}.dark{background:var(--tone-dark)}
.grey{background:var(--tone-grey)}.green{background:var(--tone-green)}.purple{background:var(--tone-purple)}
.amber{background:var(--tone-amber)}.sky{background:var(--tone-sky)}
.social{position:absolute;top:1092px;left:315px;display:flex;gap:3px}
.social span{width:23px;height:23px;border:1.3px solid var(--white);border-radius:50%}
.foot-nav{position:absolute;top:1127px;left:182px;display:flex;gap:35px;font-size:12px;font-weight:500;color:var(--white)}
.copyright{position:absolute;top:1157px;width:723px;text-align:center;padding-left:8px;font-size:9.5px;color:var(--white)}
</style>
</head>
<body>
<svg class="backdrop" viewBox="0 0 723 1200" aria-hidden="true">
  <defs>
    <linearGradient id="sky" x1="0" y1="0" x2="1" y2="0">
      <stop offset="0" stop-color="#1283f5"/><stop offset="1" stop-color="#2ab0fb"/>
    </linearGradient>
  </defs>
  <path d="M0 0H723V325C660 348 600 340 520 328C450 317 400 310 350 318C270 330 200 350 140 354C80 358 40 345 0 330Z" fill="url(#sky)"/>
  <path d="M0 1066C60 1090 130 1098 200 1086C270 1074 320 1058 380 1058C440 1058 500 1080 560 1090C630 1100 690 1080 723 1063V1200H0Z" fill="url(#sky)"/>
</svg>

<div class="brand">Glyphora</div>
<nav class="nav"><a class="current">About Us</a><a>Emoji</a><a>Collections</a><a>Top Emoji</a><a>Support</a></nav>

<h1 class="hero-title">Welcome!</h1>
<h2 class="hero-sub">Emoji Glyphora - Emoji Encyclopedia</h2>
<p class="hero-lede">Lorem ipsum dolor sit amet consectetuer adipiscing elit</p>
<div class="search">
  <svg width="16" height="16" viewBox="0 0 16 16" aria-hidden="true"><circle cx="6.5" cy="6.5" r="5" fill="none" stroke="#f39c12" stroke-width="2"/><path d="M10.2 10.2L14.5 14.5" stroke="#f39c12" stroke-width="2.4" stroke-linecap="round"/></svg>
  <span>Serach emoji</span>
</div>
<div class="hero-art rider" role="img" aria-label="Horse racing emoji illustration"></div>
<div class="hero-art surfer" role="img" aria-label="Surfer emoji illustration"></div>

<section class="card" style="left:60px;top:395px">
  <div class="card-head">Country Flags</div>
  <div class="card-grid">
    <div class="item"><div class="glyph flag" role="img" aria-label="Flag emoji" style="background:linear-gradient(#e3475b 50%,#333 50%)"></div><span class="label">Flag Title</span></div>
    <div class="item"><div class="glyph flag blue" role="img" aria-label="Flag emoji"></div><span class="label">Flag Title</span></div>
    <div class="item"><div class="glyph flag green" role="img" aria-label="Flag emoji"></div><span class="label">Flag Title</span></div>
    <div class="item"><div class="glyph flag" role="img" aria-label="Flag emoji" style="background:#2a3c8a"></div><span class="label">Flag Title</span></div>
    <div class="item"><div class="glyph flag red" role="img" aria-label="Flag emoji"></div><span class="label">Flag Title</span></div>
    <div class="item"><div class="glyph flag" role="img" aria-label="Flag emoji" style="background:linear-gradient(#e3475b 33%,#2a4fa0 33%,#2a4fa0 66%,#f0a83a 66%)"></div><span class="label">Flag Title</span></div>
  </div>
  <div class="card-foot">See all emoji</div>
</section>
<section class="card" style="left:270px;top:395px">
  <div class="card-head">Category</div>
  <div class="card-grid">
    <div class="item"><div class="glyph purple" role="img" aria-label="Medical symbol emoji"></div><span class="label">Emoji Title</span></div>
    <div class="item"><div class="glyph grey" role="img" aria-label="Crossed swords emoji"></div><span class="label">Emoji Title</span></div>
    <div class="item"><div class="glyph blue round" role="img" aria-label="Anchor emoji"></div><span class="label">Emoji Title</span></div>
    <div class="item"><div class="glyph dark round" role="img" aria-label="Gear emoji"></div><span class="label">Emoji Title</span></div>
    <div class="item"><div class="glyph sky" role="img" aria-label="Alembic emoji"></div><span class="label">Emoji Title</span></div>
    <div class="item"><div class="glyph amber" role="img" aria-label="Balance scale emoji"></div><span class="label">Emoji Title</span></div>
  </div>
  <div class="card-foot">See all emoji</div>
</section>
<section class="card" style="left:479px;top:395px">
  <div class="card-head">Cartoons</div>
  <div class="card-grid">
    <div class="item"><div class="glyph red" role="img" aria-label="Diamond suit emoji"></div><span class="label">Emoji Title</span></div>
    <div class="item"><div class="glyph red round" role="img" aria-label="Heart suit emoji"></div><span class="label">Emoji Title</span></div>
    <div class="item"><div class="glyph dark round" role="img" aria-label="Club suit emoji"></div><span class="label">Emoji Title</span></div>
    <div class="item"><div class="glyph amber" role="img" aria-label="Hammer and pick emoji"></div><span class="label">Emoji Title</span></div>
    <div class="item"><div class="glyph red" role="img" aria-label="Hot springs emoji"></div><span class="label">Emoji Title</span></div>
    <div class="item"><div class="glyph dark" role="img" aria-label="Spade suit emoji"></div><span class="label">Emoji Title</span></div>
  </div>
  <div class="card-foot">See all emoji</div>
</section>

<section class="card" style="left:62px;top:609px">
  <div class="card-head">Country Flags</div>
  <div class="card-grid">
    <div class="item"><div class="glyph flag green" role="img" aria-label="Flag emoji"></div><span class="label">Emoji Title</span></div>
    <div class="item"><div class="glyph flag red" role="img" aria-label="Flag emoji"></div><span class="label">Emoji Title</span></div>
    <div class="item"><div class="glyph flag amber" role="img" aria-label="Flag emoji"></div><span class="label">Emoji Title</span></div>
    <div class="item"><div class="glyph flag" role="img" aria-label="Flag emoji" style="background:#2a3c8a"></div><span class="label">Emoji Title</span></div>
    <div class="item"><div class="glyph flag" role="img" aria-label="Flag emoji" style="background:linear-gradient(#eee 50%,#e3475b 50%)"></div><span class="label">Emoji Title</span></div>
    <div class="item"><div class="glyph flag blue" role="img" aria-label="Flag emoji"></div><span class="label">Emoji Title</span></div>
  </div>
  <div class="card-foot">See all emoji</div>
</section>
<section class="card" style="left:272px;top:609px">
  <div class="card-head">Category</div>
  <div class="card-grid">
    <div class="item"><div class="glyph blue" role="img" aria-label="Arrow curving up emoji"></div><span class="label">Emoji Title</span></div>
    <div class="item"><div class="glyph blue" role="img" aria-label="Arrow curving right emoji"></div><span class="label">Emoji Title</span></div>
    <div class="item"><div class="glyph blue" role="img" aria-label="Arrow curving down emoji"></div><span class="label">Emoji Title</span></div>
    <div class="item"><div class="glyph blue" role="img" aria-label="Record button emoji"></div><span class="label">Emoji Title</span></div>
    <div class="item"><div class="glyph blue" role="img" aria-label="Stop button emoji"></div><span class="label">Emoji Title</span></div>
    <div class="item"><div class="glyph blue" role="img" aria-label="Back arrow emoji"></div><span class="label">Emoji Title</span></div>
  </div>
  <div class="card-foot">See all emoji</div>
</section>
<section class="card" style="left:481px;top:609px">
  <div class="card-head">Cartoons</div>
  <div class="card-grid">
    <div class="item"><div class="glyph dark" role="img" aria-label="Wavy dash emoji"></div><span class="label">Emoji Title</span></div>
    <div class="item"><div class="glyph dark round" role="img" aria-label="Registered sign emoji"></div><span class="label">Emoji Title</span></div>
    <div class="item"><div class="glyph dark round" role="img" aria-label="Copyright sign emoji"></div><span class="label">Emoji Title</span></div>
    <div class="item"><div class="glyph dark" role="img" aria-label="Plus sign emoji"></div><span class="label">Emoji Title</span></div>
    <div class="item"><div class="glyph dark" role="img" aria-label="Division sign emoji"></div><span class="label">Emoji Title</span></div>
    <div class="item"><div class="glyph dark" role="img" aria-label="Minus sign emoji"></div><span class="label">Emoji Title</span></div>
  </div>
  <div class="card-foot">See all emoji</div>
</section>

<section class="card" style="left:61px;top:823px">
  <div class="card-head">Country Flags</div>
  <div class="card-grid">
    <div class="item"><div class="glyph blue" role="img" aria-label="Pause button emoji"></div><span class="label">Emoji Title</span></div>
    <div class="item"><div class="glyph blue" role="img" aria-label="Play button emoji"></div><span class="label">Emoji Title</span></div>
    <div class="item"><div class="glyph blue" role="img" aria-label="Reverse button emoji"></div><span class="label">Emoji Title</span></div>
    <div class="item"><div class="glyph grey round" role="img" aria-label="Clock emoji"></div><span class="label">Emoji Title</span></div>
    <div class="item"><div class="glyph grey round" role="img" aria-label="Stopwatch emoji"></div><span class="label">Emoji Title</span></div>
    <div class="item"><div class="glyph blue round" role="img" aria-label="Circled letter emoji"></div><span class="label">Emoji Title</span></div>
  </div>
  <div class="card-foot">See all emoji</div>
</section>
<section class="card" style="left:271px;top:823px">
  <div class="card-head">Category</div>
  <div class="card-grid">
    <div class="item"><div class="glyph red" role="img" aria-label="Scissors emoji"></div><span class="label">Emoji Title</span></div>
    <div class="item"><div class="glyph green" role="img" aria-label="Check box emoji"></div><span class="label">Emoji Title</span></div>
    <div class="item"><div class="glyph sky" role="img" aria-label="Airplane emoji"></div><span class="label">Emoji Title</span></div>
    <div class="item"><div class="glyph grey" role="img" aria-label="Envelope emoji"></div><span class="label">Emoji Title</span></div>
    <div class="item"><div class="glyph dark" role="img" aria-label="Check mark emoji"></div><span class="label">Emoji Title</span></div>
    <div class="item"><div class="glyph dark" role="img" aria-label="Fountain pen emoji"></div><span class="label">Emoji Title</span></div>
  </div>
  <div class="card-foot">See all emoji</div>
</section>
<section class="card" style="left:480px;top:823px">
  <div class="card-head">Cartoons</div>
  <div class="card-grid">
    <div class="item"><div class="glyph sky round" role="img" aria-label="Snowflake emoji"></div><span class="label">Emoji Title</span></div>
    <div class="item"><div class="glyph dark round" role="img" aria-label="Star emoji"></div><span class="label">Emoji Title</span></div>
    <div class="item"><div class="glyph green" role="img" aria-label="Asterisk emoji"></div><span class="label">Emoji Title</span></div>
    <div class="item"><div class="glyph dark" role="img" aria-label="Cross mark emoji"></div><span class="label">Emoji Title</span></div>
    <div class="item"><div class="glyph purple" role="img" aria-label="Six pointed star emoji"></div><span class="label">Emoji Title</span></div>
    <div class="item"><div class="glyph amber round" role="img" aria-label="Sparkles emoji"></div><span class="label">Emoji Title</span></div>
  </div>
  <div class="card-foot">See all emoji</div>
</section>

<div class="social" aria-label="Social links"><span></span><span></span><span></span><span></span></div>
<nav class="foot-nav"><a>About Us</a><a>Emoji</a><a>Collections</a><a>Top Emoji</a><a>Support</a></nav>
<p class="copyright">© 2020 Company Name | All Rights Reserved</p>
</body>
</html>
```